New Billboard Design Project

Hi, Can you design another similar to 24633934, that says optimize performance with Stem Cell Therapy, or something similar. ( I was able to convert the other file. Thank you again, I appreciate all your work

```html
<!DOCTYPE html>
<html lang="en">
<head>
<meta charset="utf-8">
<title>Optimize Performance Billboards</title>
<link rel="stylesheet" href="https://fonts.googleapis.com/css2?family=Montserrat:wght@500;700;800&display=swap">
<style>
  :root {
    --navy: #283f94;
    --sky: #1a8fd0;
    --paper: #ffffff;
    --backdrop: #ececec;
    --frame: #3a3a3a;
    --rule: #b9bcc4;
    --photo-light: #e9d2c4;
    --photo-mid: #b43a2e;
    --photo-dark: #2b2f3a;
  }
  * { margin: 0; padding: 0; box-sizing: border-box; }
  html, body { width: 1200px; height: 618px; overflow: hidden; background: var(--backdrop); }
  body { position: relative; font-family: "Montserrat", Arial, sans-serif; }

  .billboard {
    position: absolute; left: 12px; width: 1180px; height: 294px;
    background: var(--paper); border: 1px solid var(--frame); overflow: hidden;
  }
  .billboard--wide { top: 6px; }
  .billboard--stacked { top: 314px; }
  .billboard > * { position: absolute; }

  .athletes-photo {
    background: linear-gradient(90deg, var(--photo-light) 0%, var(--photo-mid) 45%, var(--photo-dark) 75%, var(--photo-light) 100%);
    opacity: .85;
  }
  .billboard--wide .athletes-photo { left: 0; top: 0; width: 391px; height: 281px; }
  .billboard--stacked .athletes-photo { left: 410px; top: 50px; width: 372px; height: 225px; }

  .headline { font-weight: 800; text-transform: uppercase; letter-spacing: -0.5px; line-height: 1; white-space: nowrap; }
  .headline__lead { color: var(--sky); }
  .headline__focus { color: var(--navy); }

  .billboard--wide .headline__lead { left: 420px; width: 700px; top: 43px; font-size: 34px; text-align: center; }
  .billboard--wide .headline__focus { left: 420px; width: 700px; top: 79px; font-size: 60px; text-align: center; }

  .billboard--stacked .headline { left: 46px; top: 27px; font-size: 41px; line-height: 46.5px; }
  .billboard--stacked .headline span { display: block; }

  .brand { display: flex; align-items: center; gap: 14px; }
  .brand__dot { border-radius: 50%; background: var(--navy); flex: none; }
  .brand__name { color: var(--navy); font-weight: 700; line-height: 1; letter-spacing: 0.5px; white-space: nowrap; }
  .brand__name small { display: block; font-size: 0.4em; letter-spacing: 3px; margin-top: 10px; }

  .billboard--wide .brand { left: 395px; top: 159px; }
  .billboard--wide .brand__dot { width: 88px; height: 88px; }
  .billboard--wide .brand__name { font-size: 38px; }

  .billboard--stacked .brand { left: 716px; top: 16px; }
  .billboard--stacked .brand__dot { width: 88px; height: 88px; }
  .billboard--stacked .brand__name { font-size: 42px; }

  .divider { left: 826px; top: 177px; width: 1px; height: 80px; background: var(--rule); }

  .contact { text-align: center; font-weight: 800; line-height: 1; white-space: nowrap; }
  .contact__web { color: var(--sky); display: block; }
  .contact__phone { color: var(--navy); display: block; }

  .billboard--wide .contact { left: 840px; width: 336px; top: 173px; }
  .billboard--wide .contact__web { font-size: 30px; }
  .billboard--wide .contact__phone { font-size: 44px; margin-top: 14px; }

  .billboard--stacked .contact { left: 765px; width: 400px; top: 117px; }
  .billboard--stacked .contact__web { font-size: 32px; }
  .billboard--stacked .contact__phone { font-size: 52px; margin-top: 42px; }

  .base-band { left: 0; bottom: 0; width: 100%; }
  .billboard--wide .base-band { height: 13px; background: linear-gradient(90deg, var(--navy) 0 868px, var(--sky) 868px 100%); }
  .billboard--stacked .base-band { height: 19px; background: var(--navy); }
</style>
</head>
<body>

<section class="billboard billboard--wide">
  <div class="athletes-photo" role="img" aria-label="Group of athletes: baseball, track, football, basketball players and a boxer"></div>
  <p class="headline headline__lead">Optimize performance with</p>
  <p class="headline headline__focus">Stem cell therapy</p>
  <div class="brand">
    <span class="brand__dot"></span>
    <p class="brand__name">TRUECOURSE<small>PAIN &amp; SPINE CENTERS</small></p>
  </div>
  <span class="divider"></span>
  <p class="contact">
    <span class="contact__web">www.tcpsc.com</span>
    <span class="contact__phone">555-012-4567</span>
  </p>
  <div class="base-band"></div>
</section>

<section class="billboard billboard--stacked">
  <div class="athletes-photo" role="img" aria-label="Group of athletes: baseball, track, football, basketball players and a boxer"></div>
  <p class="headline">
    <span class="headline__lead">Optimize</span>
    <span class="headline__lead">Performance</span>
    <span class="headline__lead">With</span>
    <span class="headline__focus">Stem cell</span>
    <span class="headline__focus">Therapy</span>
  </p>
  <div class="brand">
    <span class="brand__dot"></span>
    <p class="brand__name">TRUECOURSE<small>PAIN &amp; SPINE CENTERS</small></p>
  </div>
  <p class="contact">
    <span class="contact__web">www.tcpsc.com</span>
    <span class="contact__phone">555-012-4567</span>
  </p>
  <div class="base-band"></div>
</section>

</body>
</html>
```